Illustration Design for female body shapes/ types

We need an creative and stylish illustration about female body types/ shapes for an image consultant.

```html
<!DOCTYPE html>
<html lang="en">
<head>
<meta charset="UTF-8">
<title>Female Body Shapes</title>
<link rel="stylesheet" href="https://fonts.googleapis.com/css2?family=Arimo:wght@400;700&display=swap">
<style>
  :root {
    --page-bg: #ffffff;
    --panel-blue: #3e6a8e;
    --figure-tone: #5a87ab;
    --figure-glow: #a9c6dc;
    --shape-orange: #f7931e;
    --shape-outline: #4fd0e8;
    --caption-white: #ffffff;
    --caption-edge: #1f3a52;
  }
  * { margin: 0; padding: 0; box-sizing: border-box; }
  html, body { width: 1200px; height: 675px; overflow: hidden; background: var(--page-bg); }
  .canvas { position: relative; width: 1200px; height: 675px; background: var(--page-bg); overflow: hidden; }

  .corner-accent {
    position: absolute; width: 136px; height: 63px;
    background: linear-gradient(90deg, var(--shape-orange) 0 50%, var(--shape-outline) 50% 100%);
  }
  .corner-accent.top-left { left: 0; top: 0; }
  .corner-accent.top-right { right: 0; top: 0; }
  .corner-accent.bottom-left { left: 0; bottom: 0; }
  .corner-accent.bottom-right { right: 0; bottom: 0; }

  .panel {
    position: absolute; left: 69px; top: 60px; width: 1062px; height: 553px;
    background: var(--panel-blue);
  }

  .body-type { position: absolute; top: 100px; width: 120px; height: 490px; }

  .figure-art {
    position: absolute; left: 14px; top: 0; width: 92px; height: 420px;
    border-radius: 46px 46px 30px 30px;
    background: linear-gradient(180deg, var(--figure-tone) 0%, #52809f 60%, #4a7698 100%);
    box-shadow: 0 0 10px 3px rgba(169,198,220,0.55), inset 0 0 6px rgba(169,198,220,0.5);
  }

  .shape-mark { position: absolute; left: 0; top: 0; width: 120px; height: 427px; }
  .shape-mark .fill { fill: var(--shape-orange); }
  .shape-mark .outline { fill: var(--shape-orange); stroke: var(--shape-outline); stroke-width: 3; stroke-linejoin: miter; }
  .shape-mark .halo { fill: var(--shape-outline); stroke: var(--shape-outline); stroke-width: 6; }

  .caption {
    position: absolute; left: -30px; width: 180px; top: 443px;
    text-align: center;
    font-family: "Arimo", Arial, sans-serif; font-size: 21px; line-height: 22px;
    color: var(--caption-white);
    text-shadow: 0 0 2px var(--caption-edge), 0 0 2px var(--caption-edge), 0 0 3px var(--caption-edge);
    letter-spacing: -0.3px;
  }
  .caption.two-line { top: 430px; }
</style>
</head>
<body>
<div class="canvas">
  <div class="corner-accent top-left" role="img" aria-label="Orange and cyan corner ornament"></div>
  <div class="corner-accent top-right" role="img" aria-label="Orange and cyan corner ornament"></div>
  <div class="corner-accent bottom-left" role="img" aria-label="Orange and cyan corner ornament"></div>
  <div class="corner-accent bottom-right" role="img" aria-label="Orange and cyan corner ornament"></div>

  <div class="panel"></div>

  <div class="body-type" style="left:147px">
    <div class="figure-art" role="img" aria-label="Line drawing of a standing woman with a rectangle body shape"></div>
    <svg class="shape-mark" viewBox="0 0 120 427" aria-hidden="true">
      <rect class="outline" x="33" y="96" width="56" height="108"/>
    </svg>
    <p class="caption">Rectangle</p>
  </div>

  <div class="body-type" style="left:304px">
    <div class="figure-art" role="img" aria-label="Line drawing of a standing woman with a pear body shape"></div>
    <svg class="shape-mark" viewBox="0 0 120 427" aria-hidden="true">
      <circle class="halo" cx="60" cy="122" r="24"/>
      <circle class="halo" cx="60" cy="167" r="40"/>
      <circle class="fill" cx="60" cy="122" r="24"/>
      <circle class="fill" cx="60" cy="167" r="40"/>
    </svg>
    <p class="caption">Pear</p>
  </div>

  <div class="body-type" style="left:464px">
    <div class="figure-art" role="img" aria-label="Line drawing of a standing woman with an hourglass body shape"></div>
    <svg class="shape-mark" viewBox="0 0 120 427" aria-hidden="true">
      <path class="outline" d="M27,100 L93,100 Q72,150 93,200 L27,200 Q48,150 27,100 Z"/>
    </svg>
    <p class="caption">Hourglass</p>
  </div>

  <div class="body-type" style="left:617px">
    <div class="figure-art" role="img" aria-label="Line drawing of a standing woman with an oval body shape"></div>
    <svg class="shape-mark" viewBox="0 0 120 427" aria-hidden="true">
      <ellipse class="outline" cx="60" cy="150" rx="34" ry="58"/>
    </svg>
    <p class="caption">Oval</p>
  </div>

  <div class="body-type" style="left:776px">
    <div class="figure-art" role="img" aria-label="Line drawing of a standing woman with an inverted triangle body shape"></div>
    <svg class="shape-mark" viewBox="0 0 120 427" aria-hidden="true">
      <path class="outline" d="M27,100 L93,100 L60,196 Z"/>
    </svg>
    <p class="caption two-line">Inverted<br>Triangle</p>
  </div>

  <div class="body-type" style="left:933px">
    <div class="figure-art" role="img" aria-label="Line drawing of a standing woman with a triangle body shape"></div>
    <svg class="shape-mark" viewBox="0 0 120 427" aria-hidden="true">
      <path class="outline" d="M60,98 L96,196 L24,196 Z"/>
    </svg>
    <p class="caption">Triangle</p>
  </div>
</div>
</body>
</html>
```